One page sales fact sheet for data consultancy company

We need a serious and professional looking 1-page fact sheet that we want to send over to potential clients via email.
The upper part should consists of a header, the client logo and 3 charts.
(1 chart with 5 datapoints / 1 chart with 3 bubbles and percentage in it, 1 chart with numbers and text)
In the lower part there should be some text description about our company and a big chart consisting of a table (see drawing).
See attached drawing to get a better understanding of the whole idea.
The fact sheet should be catchy but professional in the same way.
Colors your choice but classic, i.e. black/white/grey/blue
The contest winner can expect more work from us based on the winning design.
*Please note that the logo reflects our original logo style but is not our
actual company name for privacy reasons

```html
<!DOCTYPE html>
<html lang="en">
<head>
<meta charset="utf-8">
<title>Norvik Market Analysis Fact Sheet</title>
<link rel="stylesheet" href="https://fonts.googleapis.com/css2?family=Barlow:wght@400;700&family=Barlow+Condensed:wght@400;500;600;700&family=Open+Sans:wght@300;700&display=swap">
<style>
  :root {
    --cyan: #00b5e8;
    --sky: #6dcff6;
    --pale: #b3e3f7;
    --mid: #0e6bbf;
    --navy: #164880;
    --frame: #1b4a8a;
    --text-blue: #1b4a8a;
    --link-blue: #1b75bb;
    --red: #d0202e;
    --grey: #777a7d;
    --paper: #ffffff;
    --backdrop: #d9d9d9;
  }
  * { margin: 0; padding: 0; box-sizing: border-box; }
  html, body { width: 1200px; height: 1200px; overflow: hidden; background: var(--backdrop); }
  .canvas { position: relative; width: 1200px; height: 1200px; }
  .sheet {
    position: absolute; left: 175px; top: 50px;
    width: 886px; height: 1145px; background: var(--paper);
    transform: scale(0.96); transform-origin: top left;
    box-shadow: 0 6px 24px rgba(0,0,0,.25);
    overflow: hidden;
    font-family: 'Barlow Condensed', sans-serif;
  }
  .abs { position: absolute; }
  .top-band {
    left: 57px; top: 0; width: 773px; height: 61px; background: var(--cyan);
    color: #fff; font-family: 'Barlow', sans-serif; font-size: 21px; letter-spacing: 9px;
    display: flex; align-items: center; justify-content: center; padding-left: 9px;
  }
  .frame { left: 0; top: 0; width: 886px; height: 1145px; }
  .brand-name {
    left: 0; width: 886px; top: 70px; text-align: center;
    font-family: 'Barlow', sans-serif; font-weight: 700; font-size: 76px;
    color: var(--navy); letter-spacing: -1px;
  }
  .logo-word {
    left: 0; width: 886px; top: 172px; text-align: center;
    font-family: 'Open Sans', sans-serif; font-weight: 700; font-size: 64px; color: var(--red);
  }
  .product-name {
    left: 0; width: 886px; top: 256px; text-align: center;
    font-family: 'Open Sans', sans-serif; font-weight: 300; font-size: 38px; color: var(--red);
  }
  .section-tag {
    height: 54px; background: var(--pale); color: var(--link-blue);
    font-family: 'Barlow', sans-serif; font-size: 22px; line-height: 20px;
  }
  .tag-data { left: 0; top: 263px; width: 215px; clip-path: polygon(0 0, 100% 0, 94% 100%, 0 100%); padding: 8px 0 0 105px; }
  .tag-types { left: 660px; top: 263px; width: 226px; clip-path: polygon(0 0, 100% 0, 100% 100%, 6% 100%); padding: 8px 96px 0 0; text-align: right; }
  .tag-steps { left: 0; top: 863px; width: 204px; clip-path: polygon(0 0, 100% 0, 94% 100%, 0 100%); padding: 15px 0 0 94px; }
  .chart { left: 0; top: 0; width: 886px; height: 470px; }
  .chart-label { font-family: 'Barlow Condensed', sans-serif; font-size: 10px; fill: #333; }
  .bubble-value { font-family: 'Open Sans', sans-serif; font-weight: 700; fill: #fff; }
  .stats { left: 0; width: 886px; top: 476px; text-align: center; font-weight: 700; font-size: 38px; line-height: 33px; }
  .stat-grey { color: var(--grey); }
  .stat-navy { color: var(--navy); }
  .stat-cyan { color: var(--cyan); }
  .watermark {
    left: 0; width: 886px; top: 640px; text-align: center;
    font-family: 'Barlow', sans-serif; font-weight: 700; font-size: 170px; color: #eaf6fd;
  }
  .about { left: 62px; width: 762px; top: 641px; text-align: center; color: var(--text-blue); font-size: 15px; line-height: 19px; }
  .about p { margin-bottom: 8px; }
  .about .highlight { color: var(--link-blue); }
  .steps { left: 0; top: 0; width: 886px; height: 1145px; }
  .step-text { font-family: 'Barlow', sans-serif; font-size: 16px; letter-spacing: 7px; fill: #fff; }
  .row-text { font-family: 'Barlow', sans-serif; font-size: 11px; letter-spacing: 2px; fill: #fff; }
  .foot-band {
    left: 57px; top: 1088px; width: 773px; height: 57px; background: var(--cyan);
    color: #fff; font-family: 'Barlow', sans-serif; font-size: 12px; letter-spacing: 3px;
    display: flex; align-items: center; justify-content: center; gap: 6px;
  }
  .foot-band svg { width: 16px; height: 16px; flex: none; }
</style>
</head>
<body>
<div class="canvas">
  <div class="sheet">
    <div class="abs top-band">MARKET ANALYSIS</div>

    <svg class="abs frame" viewBox="0 0 886 1145" aria-hidden="true">
      <g fill="none" stroke="var(--frame)" stroke-width="4">
        <polyline points="305,106 59,106 59,553 140,553"/>
        <polyline points="115,523 142,553 115,582"/>
        <polyline points="580,106 827,106 827,553 746,553"/>
        <polyline points="772,523 745,553 772,582"/>
      </g>
    </svg>

    <div class="abs brand-name">NORVIK</div>
    <div class="abs logo-word">LOGO</div>
    <div class="abs product-name">[product name]</div>

    <div class="abs section-tag tag-data">DATA<br>POINTS</div>
    <div class="abs section-tag tag-types">PRODUCT<br>TYPES</div>

    <svg class="abs chart" viewBox="0 0 886 470" role="img" aria-label="Bar chart and bubble chart of product categories">
      <rect x="105" y="353" width="63" height="78" fill="var(--sky)"/>
      <rect x="168" y="329" width="63" height="102" fill="var(--navy)"/>
      <rect x="231" y="365" width="63" height="66" fill="var(--mid)"/>
      <rect x="294" y="398" width="63" height="33" fill="var(--cyan)"/>
      <text class="chart-label" x="135" y="449" text-anchor="middle">PHARETRA</text>
      <text class="chart-label" x="199" y="449" text-anchor="middle">TORTOR</text>
      <text class="chart-label" x="260" y="449" text-anchor="middle">POSUERE</text>
      <text class="chart-label" x="323" y="449" text-anchor="middle">VULPUTATE</text>

      <circle cx="558" cy="380" r="50" fill="var(--sky)"/>
      <circle cx="652" cy="393" r="38" fill="var(--cyan)"/>
      <circle cx="722" cy="405" r="26" fill="var(--mid)"/>
      <circle cx="765" cy="417" r="12" fill="var(--navy)"/>
      <text class="bubble-value" x="555" y="396" font-size="44" text-anchor="middle">40<tspan font-size="20" dy="-18">%</tspan></text>
      <text class="bubble-value" x="650" y="405" font-size="34" text-anchor="middle">30<tspan font-size="16" dy="-14">%</tspan></text>
      <text class="bubble-value" x="720" y="413" font-size="22" text-anchor="middle">20<tspan font-size="11" dy="-9">%</tspan></text>
      <text class="bubble-value" x="764" y="421" font-size="10" text-anchor="middle">10<tspan font-size="5" dy="-4">%</tspan></text>
      <text class="chart-label" x="562" y="449" text-anchor="middle">PHARETRA</text>
      <text class="chart-label" x="652" y="449" text-anchor="middle">TORTOR</text>
      <text class="chart-label" x="719" y="449" text-anchor="middle">POSUERE</text>
      <text class="chart-label" x="763" y="449" text-anchor="middle">VULPUTATE</text>
    </svg>

    <div class="abs stats">
      <div class="stat-grey">20 VENDORS</div>
      <div class="stat-navy">150 PRODUCTS</div>
      <div class="stat-cyan">350.000 AVAILABLE ITEMS</div>
      <div class="stat-navy">40 MILLION IN SALES</div>
    </div>

    <div class="abs watermark" aria-hidden="true">NORVIK</div>
    <div class="abs about">
      <p>Lorem ipsum dolor sit amet, consectetur adipiscing elit. Sed venenatis ante fermentum elit convallis tristique. Aliquam erat volutpat. Proin sit amet dui pharetra tortor posuere vulputate. Sed elit mauris, efficitur non blandit non, auctor id nisl.</p>
      <p>Vivamus facilisis quam dui, at eleifend odio rhoncus sagittis. Nam sollicitudin pulvinar volutpat. Sed ac libero lacus. Fusce iaculis ligula tincidunt nisi vestibulum imperdiet. Quisque ornare justo in arcu placerat malesuada. Maecenas non velit condimentum, placerat turpis et, suscipit arcu. Cras urna lorem, semper ultrices consectetur ac, volutpat rutrum neque. Maecenas at bibendum mauris.</p>
      <p>Mauris aliquet dapibus tellus, et vulputate enim placerat sed. Nulla id feugiat sem.<br>Suspendisse vel sapien quis urna fermentum feugiat.</p>
      <p class="highlight">Mauris a massa interdum, lacinia nisi non, maximus diam. Vestibulum et nisl a ante dictum fringilla.</p>
    </div>

    <div class="abs section-tag tag-steps">STEPS</div>

    <svg class="abs steps" viewBox="0 0 886 1145" role="img" aria-label="Layered steps diagram from competitors to personal level">
      <polyline points="95,941 210,941 216,907 456,907 449,931" fill="none" stroke="#999" stroke-width="2"/>
      <polyline points="95,941 95,957 320,957" fill="none" stroke="#999" stroke-width="2"/>
      <text x="336" y="926" font-family="Barlow, sans-serif" font-size="16" letter-spacing="7" fill="#666" text-anchor="middle">COMPETITORS</text>

      <rect x="95" y="966" width="350" height="17" fill="var(--cyan)"/>
      <polygon points="325,932 562,932 550,983 315,983" fill="var(--cyan)"/>
      <rect x="95" y="991" width="455" height="17" fill="var(--mid)"/>
      <polygon points="446,958 683,958 672,1008 436,1008" fill="var(--mid)"/>
      <rect x="95" y="1016" width="460" height="18" fill="var(--navy)"/>
      <polygon points="555,983 795,983 780,1034 545,1034" fill="var(--navy)"/>

      <text class="step-text" x="440" y="952" text-anchor="middle">USER LAYER</text>
      <text class="step-text" x="560" y="978" text-anchor="middle">ENTITY LAYER</text>
      <text class="step-text" x="674" y="1003" text-anchor="middle">PERSONAL</text>
      <text class="step-text" x="674" y="1024" text-anchor="middle">LEVEL</text>

      <text class="row-text" x="106" y="953" fill="#777" style="fill:#777">LAYER 1</text>
      <text class="row-text" x="106" y="979">LAYER 2</text>
      <text class="row-text" x="106" y="1004">LAYER 3</text>
      <text class="row-text" x="106" y="1030">LAYER 4</text>

      <g fill="none" stroke="var(--navy)" stroke-width="1.5">
        <polyline points="582,933 815,933 815,1037 799,1037"/>
        <polyline points="588,928 581,933 588,938"/>
        <polyline points="805,1032 798,1037 805,1042"/>
      </g>
      <text x="766" y="961" font-family="Barlow, sans-serif" font-weight="700" font-size="27" fill="var(--navy)" text-anchor="middle">NORVIK</text>
    </svg>

    <div class="abs foot-band">
      <span>MARKET ANALYSIS | NORVIK |</span>
      <svg viewBox="0 0 16 16" aria-hidden="true"><circle cx="8" cy="8" r="8" fill="#fff"/><rect x="4" y="4.5" width="8" height="5.5" fill="none" stroke="var(--cyan)" stroke-width="1.4"/><line x1="6" y1="12" x2="10" y2="12" stroke="var(--cyan)" stroke-width="1.4"/></svg>
      <span>WWW.NORVIK.COM</span>
      <svg viewBox="0 0 16 16" aria-hidden="true"><circle cx="8" cy="8" r="8" fill="#fff"/><path d="M5.5 4 L7 4 L7.6 6.2 L6.6 7 Q7.5 9 9 9.6 L9.8 8.6 L12 9.2 L12 10.7 Q8 11.5 5 7 Q4.8 5 5.5 4 Z" fill="var(--cyan)"/></svg>
      <span>9999 9999 999</span>
      <svg viewBox="0 0 16 16" aria-hidden="true"><circle cx="8" cy="8" r="8" fill="#fff"/><rect x="4" y="5" width="8" height="6" fill="none" stroke="var(--cyan)" stroke-width="1.3"/><polyline points="4,5 8,8.5 12,5" fill="none" stroke="var(--cyan)" stroke-width="1.3"/></svg>
      <span>ENQUIRIES@NORVIK.COM</span>
    </div>
  </div>
</div>
</body>
</html>
```